Postcard Needed for scooter business to entice retail customers

Company: Harbor Wellness & Living cobranded with Keel Motion
Specs: 6" x 9" high-res InDesign files with bleeds
Target Audience: Potential customer's who called Harbor about the Feathra Scooter, but did not buy
Objective: To entice these potential customers to buy a Feathra Scooter from a retail partner near them named Keel Motion with a $100 off discount
Creative Direction:
The postcard should feature Harbor colors and images of the The Feathra Scooter with the Harbor Feathra logo. The logo for Keel Motion (retail location) should also be included.
The discount should be prominently displayed and have instructions on bringing it in to redeem in-person with the location address
Copy:
FRONT
Headline: Save $100 when you come in today!
Bullet points to include:
- The super-light frame (about 40 lbs) is much lighter than many traditional models, making it easier to transport.
-It folds in seconds: nothing has to be removed, good for air, cruise, car, train travel.
- Electronic stability control helps prevent tipping by slowing down when going into a turn.
BACK
Visit Keel Motion Scooters today at
20417 State Road 82
Dunmore, FL 33218
For $100 OFF the Harbor Feathra Scooter!
Style Guide & Harbor Logos: https://brightvale.example-assets.com/g/HarborStyleGuide
Feathra Scooter Images: https://brightvale.example-assets.com/b/Q82KT
Keel Motion logo: attached
Target Market(s)
Previous caller, who did not buy, age 65+
Colors
Designer to choose colors to be used in the design.
Requirements
Must have
- larger font and saturated colors for older eyes

```html
<!DOCTYPE html>
<html lang="en">
<head>
<meta charset="utf-8">
<title>Harbor Wellness &amp; Living – Feathra Scooter Postcard Front</title>
<link rel="stylesheet" href="https://fonts.googleapis.com/css2?family=Montserrat:wght@500;600;700;800&display=swap">
<style>
  :root {
    --page-bg: #d9d9d9;
    --brand-blue: #3b7fc6;
    --brand-blue-deep: #2d68b0;
    --brand-blue-light: #5c9bd9;
    --ink-white: #ffffff;
    --photo-green: #5f7f3e;
    --photo-stone: #b9ab98;
    --photo-dark: #141414;
    --thumb-frame: #ffffff;
  }
  * { box-sizing: border-box; margin: 0; padding: 0; }
  html, body {
    width: 1200px; height: 850px; overflow: hidden;
    background: var(--page-bg);
    font-family: "Montserrat", Arial, sans-serif;
  }
  .postcard {
    position: absolute; left: 0; top: 25px;
    width: 1200px; height: 800px; overflow: hidden;
    background: var(--photo-dark);
  }
  .hero-photo {
    position: absolute; inset: 0;
    background:
      radial-gradient(ellipse 55% 60% at 85% 25%, rgba(10,10,10,0.95), rgba(10,10,10,0) 70%),
      linear-gradient(180deg, rgba(0,0,0,0) 55%, rgba(80,110,50,0.9) 78%),
      linear-gradient(90deg, var(--photo-stone) 0%, #8f8a78 22%, #4e5a3a 40%, #1e2418 62%, var(--photo-dark) 100%);
  }
  .feature-band { position: absolute; inset: 0; }
  .offer-pill {
    position: absolute; left: 568px; top: 86px;
    width: 487px; height: 101px;
    border: 3px solid var(--ink-white); border-radius: 51px;
    background: rgba(0,0,0,0.55);
    overflow: hidden;
  }
  .offer-pill__save {
    position: absolute; left: 24px; top: 0; width: 226px; height: 95px;
    display: flex; align-items: center; justify-content: center;
    color: var(--ink-white); font-weight: 700; font-size: 76px; letter-spacing: 0;
  }
  .offer-pill__amount {
    position: absolute; left: 254px; top: 0; right: 0; height: 95px;
    background: var(--brand-blue);
    display: flex; align-items: center; justify-content: center;
    color: var(--ink-white); font-weight: 700; font-size: 76px;
    text-shadow: 0 3px 4px rgba(0,0,0,0.35);
  }
  .headline {
    position: absolute; left: 560px; width: 506px; top: 204px;
    text-align: center; color: var(--ink-white);
    font-weight: 500; font-size: 55px; line-height: 62px;
  }
  .feature {
    position: absolute; top: 387px; width: 220px;
    display: flex; flex-direction: column; align-items: center;
  }
  .feature--weight { left: 461px; }
  .feature--fold { left: 703px; }
  .feature--stability { left: 943px; }
  .feature__photo {
    width: 202px; height: 119px;
    border: 6px solid var(--thumb-frame);
    box-shadow: 0 4px 8px rgba(0,0,0,0.4);
  }
  .feature--weight .feature__photo { background: linear-gradient(135deg, #d8c9b2, #6b7a8c 55%, #2f4e86); }
  .feature--fold .feature__photo { background: linear-gradient(135deg, #b9c3c6, #5b6167 55%, #7fae5a); }
  .feature--stability .feature__photo { background: linear-gradient(135deg, #4d4a47, #7a94b8 50%, #c9a58c); }
  .feature__text {
    margin-top: 22px; text-align: center; color: var(--ink-white);
    font-weight: 500; font-size: 18px; line-height: 24px;
  }
</style>
</head>
<body>
  <main class="postcard">
    <div class="hero-photo" role="img" aria-label="Smiling senior woman riding a blue Feathra folding scooter on a garden sidewalk, walking beside her younger companion, with a house and trees behind"></div>

    <svg class="feature-band" width="1200" height="800" viewBox="0 0 1200 800" aria-hidden="true">
      <defs>
        <linearGradient id="bandFill" x1="0" y1="0" x2="1" y2="1">
          <stop offset="0" stop-color="#4d8fd2"/>
          <stop offset="1" stop-color="#2d68b0"/>
        </linearGradient>
      </defs>
      <polygon points="384,452 1200,452 1200,800 930,800" fill="url(#bandFill)"/>
      <polygon points="384,452 430,452 975,800 930,800" fill="#5c9bd9" opacity="0.55"/>
    </svg>

    <div class="offer-pill">
      <span class="offer-pill__save">SAVE</span>
      <span class="offer-pill__amount">$100</span>
    </div>

    <h1 class="headline">WHEN YOU<br>COME IN TODAY!</h1>

    <section class="feature feature--weight">
      <div class="feature__photo" role="img" aria-label="Person lifting the lightweight scooter on a porch"></div>
      <p class="feature__text">The super-light frame (about 40 lbs) is much lighter than many traditional models, making it easier to transport.</p>
    </section>

    <section class="feature feature--fold">
      <div class="feature__photo" role="img" aria-label="Folded scooter stored in the open trunk of a car"></div>
      <p class="feature__text">It folds in seconds: nothing has to be removed, good for air, cruise, car, train travel.</p>
    </section>

    <section class="feature feature--stability">
      <div class="feature__photo" role="img" aria-label="Hand on the scooter control panel knob"></div>
      <p class="feature__text">Electronic stability control helps prevent tipping by slowing down when going into a turn.</p>
    </section>
  </main>
</body>
</html>
```